Cover design of Conference Program

We need a cover design of our conference program for association consisting of Middle East studies scholars. The design should compliment and incorporate the conference logo and colors.

```html
<!DOCTYPE html>
<html lang="en">
<head>
<meta charset="utf-8">
<title>LSS 2022 Conference Program Cover</title>
<link rel="stylesheet" href="https://fonts.googleapis.com/css2?family=Cinzel:wght@600&family=PT+Sans:wght@400;700&family=Montserrat:wght@400&display=swap">
<style>
  :root {
    --backdrop: #ebebeb;
    --paper: #ffffff;
    --gold: #d3b06c;
    --gold-soft: #d9ba7a;
    --navy: #1f3a88;
    --purple: #6f4a9c;
    --mist: #f1f1f3;
    --haze: #ececf2;
  }
  html, body {
    margin: 0;
    padding: 0;
    width: 1200px;
    height: 2234px;
    overflow: hidden;
    background: var(--backdrop);
  }
  .program-cover {
    position: absolute;
    left: 50px;
    top: 405px;
    width: 1100px;
    height: 1423px;
    box-shadow: 0 18px 40px rgba(0,0,0,0.18);
    background: var(--paper);
  }
  .program-cover svg { display: block; width: 100%; height: 100%; }
  .brand-name { font-family: "PT Sans", sans-serif; font-weight: 700; fill: var(--navy); }
  .brand-meta { font-family: "PT Sans", sans-serif; font-weight: 400; fill: var(--purple); }
  .title-small { font-family: "Cinzel", serif; font-weight: 600; fill: var(--purple); }
  .title-main { font-family: "Cinzel", serif; font-weight: 600; fill: var(--navy); }
  .site-url { font-family: "Montserrat", sans-serif; font-weight: 400; fill: var(--purple); }
  .footer-name { font-family: "PT Sans", sans-serif; font-weight: 700; fill: var(--paper); }
</style>
</head>
<body>
  <div class="program-cover">
    <svg viewBox="0 0 920 1190" xmlns="http://www.w3.org/2000/svg">
      <defs>
        <linearGradient id="photoTone" x1="0" y1="0" x2="1" y2="1">
          <stop offset="0" stop-color="#d9cdbd"/>
          <stop offset="0.5" stop-color="#b98a6a"/>
          <stop offset="1" stop-color="#c8494a"/>
        </linearGradient>
      </defs>

      <rect class="paper" width="920" height="1190" fill="var(--paper)"/>

      <polygon class="pattern-corner" role="img" aria-label="Faint geometric pattern decoration"
               points="578,0 920,0 920,245" fill="var(--haze)"/>

      <polygon class="gray-facet" points="618,540 920,405 920,752" fill="var(--mist)"/>

      <polygon class="gold-field" points="0,265 920,908 920,1190 0,1190" fill="var(--gold)"/>

      <polygon class="blue-facet" points="661,93 920,275 920,410 621,527" fill="var(--navy)"/>
      <polygon class="purple-facet" points="461,433 626,358 610,532" fill="var(--purple)"/>
      <polygon class="purple-facet-small" points="576,668 648,633 641,710" fill="var(--purple)"/>

      <polygon class="photo-frame" points="321,350 680,603 275,795" fill="var(--paper)"
               stroke="var(--paper)" stroke-width="14" stroke-linejoin="miter"/>
      <polygon class="photo-slot" role="img" aria-label="Photo of students studying together around a laptop"
               points="321,350 680,603 275,795" fill="url(#photoTone)"/>

      <!-- Brand lockup -->
      <rect class="brand-square" x="178" y="66" width="70" height="70" fill="var(--gold)"/>
      <line class="brand-rule" x1="75" y1="140" x2="356" y2="140" stroke="var(--purple)" stroke-width="1.5"/>
      <text class="brand-name" x="75" y="198" font-size="54" textLength="281" lengthAdjust="spacingAndGlyphs">LSS 2022</text>
      <text class="brand-meta" x="75" y="226" font-size="19" textLength="282" lengthAdjust="spacingAndGlyphs">Ashford, Montana | December 1-4</text>

      <!-- Title block -->
      <line class="title-rule" x1="218" y1="861" x2="325" y2="861" stroke="var(--purple)" stroke-width="1.5"/>
      <line class="title-rule" x1="596" y1="861" x2="703" y2="861" stroke="var(--purple)" stroke-width="1.5"/>
      <text class="title-small" x="340" y="873" font-size="34" textLength="241" lengthAdjust="spacingAndGlyphs">LEVANT REGION</text>
      <text class="title-small" x="215" y="914" font-size="44" textLength="493" lengthAdjust="spacingAndGlyphs">SCHOLARS SOCIETY</text>
      <text class="title-main" x="65" y="974" font-size="72" textLength="788" lengthAdjust="spacingAndGlyphs">56TH ANNUAL MEETING</text>

      <rect class="url-box" x="311" y="1011" width="299" height="38" fill="none" stroke="var(--paper)" stroke-width="1.2" opacity="0.8"/>
      <text class="site-url" x="333" y="1037" font-size="19" textLength="257" lengthAdjust="spacing">www.lss-meet.org</text>

      <!-- Footer -->
      <text class="footer-name" x="460" y="1116" font-size="28" text-anchor="middle">LSS</text>
      <line class="footer-rule" x1="0" y1="1123" x2="790" y2="1123" stroke="var(--paper)" stroke-width="2.5"/>

      <rect class="corner-ornament-left" role="img" aria-label="Decorative corner ornament"
            x="0" y="1130" width="100" height="60" fill="var(--gold-soft)"/>
      <rect class="corner-ornament-right" role="img" aria-label="Decorative triangle ornament cluster"
            x="785" y="1062" width="135" height="128" fill="var(--gold-soft)"/>
    </svg>
  </div>
</body>
</html>
```